Qorvani Holdings Business Card

Create a two sided, high gloss, quality business card for Qorvani Holdings.

Target Market(s)

People wanting to purchase, scale, and sell businesses.

Industry/Entity Type

Entrepreneurs

Contact Information for Business Card

One line: Tessa Ruble, CPA, CMA Another line: Entrepreneur & Investor Another line: Business Ownership Transition Expert Another line: Multi-State Licensed Real Estate Broker Phone 954-QORVANI (767-8264) Email Tessa@Qorvani Holdings.com Website www.Qorvani.com

Requirements
Must have
• Black Card, logo on one side, all other information on the other side including a small logo.
Nice to have
• Possibly add a tagline "Helping entrepreneurs live a life they don't need a vacation from"
Should not have
• There will not be a mailing address on these cards.

```html
<!DOCTYPE html>
<html lang="en">
<head>
<meta charset="utf-8">
<title>Qorvani Holdings Business Card</title>
<link rel="stylesheet" href="https://fonts.googleapis.com/css2?family=Montserrat:wght@400;600;700&display=swap">
<style>
  :root {
    --backdrop: #f1f1f1;
    --card: #070708;
    --gold: #d9b44a;
    --gold-light: #f3dc8a;
    --gold-deep: #a67c1e;
    --ink-light: #f2f2f2;
  }
  * { box-sizing: border-box; margin: 0; padding: 0; }
  html, body {
    width: 1200px; height: 1200px; overflow: hidden;
    background: var(--backdrop);
    font-family: "Montserrat", sans-serif;
  }
  .card {
    position: absolute;
    left: 167px;
    width: 865px; height: 519px;
    background: var(--card);
    overflow: hidden;
  }
  .card--front { top: 71px; }
  .card--back { top: 634px; }
  .front-arc { position: absolute; left: 0; top: 0; }
  .brand {
    position: absolute;
    display: flex; align-items: center; gap: 12px;
    color: var(--gold);
    font-weight: 700;
    white-space: nowrap;
  }
  .brand__dot {
    border-radius: 50%;
    border: 3px solid var(--gold);
  }
  .brand--small { right: 58px; top: 98px; font-size: 34px; }
  .brand--small .brand__dot { width: 26px; height: 26px; }
  .brand--large {
    left: 50%; top: 50%; transform: translate(-50%, -50%);
    font-size: 56px; gap: 18px;
  }
  .brand--large .brand__dot { width: 40px; height: 40px; border-width: 4px; }
  .holder { position: absolute; left: 55px; top: 196px; }
  .holder__name {
    color: var(--gold);
    font-weight: 700;
    font-size: 28px;
    letter-spacing: 0.5px;
    margin-bottom: 14px;
  }
  .holder__role {
    color: var(--ink-light);
    font-size: 18px;
    line-height: 24px;
    letter-spacing: 0.3px;
  }
  .contact { position: absolute; left: 55px; top: 382px; list-style: none; }
  .contact__item {
    display: flex; align-items: center;
    color: var(--ink-light);
    font-size: 20.5px;
    height: 26.5px;
    letter-spacing: 0.3px;
  }
  .contact__icon { width: 14px; height: 14px; margin-right: 17px; fill: var(--gold); }
</style>
</head>
<body>
  <section class="card card--front">
    <svg class="front-arc" width="865" height="519" viewBox="0 0 865 519" aria-hidden="true">
      <defs>
        <linearGradient id="arcGold" x1="0" y1="0" x2="1" y2="1">
          <stop offset="0" stop-color="var(--gold-deep)"/>
          <stop offset="0.45" stop-color="var(--gold-light)"/>
          <stop offset="1" stop-color="var(--gold)"/>
        </linearGradient>
      </defs>
      <path d="M0,198 C150,25 520,45 518,405" fill="none" stroke="url(#arcGold)" stroke-width="7" stroke-linecap="round"/>
    </svg>

    <div class="brand brand--small"><span class="brand__dot"></span>Qorvani Holdings</div>

    <div class="holder">
      <h1 class="holder__name">Tessa Ruble, CPA, CMA</h1>
      <p class="holder__role">Entrepreneur &amp; Investor</p>
      <p class="holder__role">Business Ownership Transition Expert</p>
      <p class="holder__role">Multi-State Licensed Real Estate Broker</p>
    </div>

    <ul class="contact">
      <li class="contact__item">
        <svg class="contact__icon" viewBox="0 0 24 24" aria-hidden="true"><path d="M6.6 10.8a15 15 0 0 0 6.6 6.6l2.2-2.2c.3-.3.7-.4 1-.2 1.1.4 2.3.6 3.6.6.6 0 1 .4 1 1V20c0 .6-.4 1-1 1A17 17 0 0 1 3 4c0-.6.4-1 1-1h3.5c.6 0 1 .4 1 1 0 1.3.2 2.5.6 3.6.1.3 0 .7-.2 1z"/></svg>
        954-QORVANI (767-8264)
      </li>
      <li class="contact__item">
        <svg class="contact__icon" viewBox="0 0 24 24" aria-hidden="true"><path d="M2 5h20v14H2z M3.5 6.5 12 13l8.5-6.5" /></svg>
        Tessa@Qorvani Holdings.com
      </li>
      <li class="contact__item">
        <svg class="contact__icon" viewBox="0 0 24 24" aria-hidden="true"><circle cx="12" cy="12" r="10"/></svg>
        www.Qorvani.com
      </li>
    </ul>
  </section>

  <section class="card card--back">
    <div class="brand brand--large"><span class="brand__dot"></span>Qorvani Holdings</div>
  </section>
</body>
</html>
```